Church Lanterns Over Millbrook Gospel Booklet Design

We need a booklet designed that we will be printing to hand out in our community. Wording for each page will be provided and we need graphic design to produce the layouts in a format ready for print. Booklet will be 4.75" x 4.75" square and a total of 12 pages: 1 cover page front, 1 cover page back, 10 inside pages some of which will be full spread across 2 pages.

Target Market(s)

English speaking Westerners

Industry/Entity Type

Religious

Font styles to use
Serif

Colors
ffffff
85abd2
0292cd
33b8a4
5c5c5c

Requirements
Must have
• Minimalist design with clean look described in attached document
Nice to have
• Aesthetically pleasing graphics, crisp fonts, excellent turn around times
Should not have
• Effeminate design, busy look with too much graphic and text

```html
<!DOCTYPE html>
<html lang="en">
<head>
<meta charset="utf-8">
<title>Lanterns Over Millbrook – Booklet Spreads</title>
<link href="https://fonts.googleapis.com/css2?family=Roboto:ital,wght@0,400;0,700;1,400&family=Oswald:wght@500;700&display=swap" rel="stylesheet">
<style>
  :root {
    --backdrop: #000000;
    --paper: #ffffff;
    --ink: #2b2b2b;
    --ink-soft: #5c5c5c;
    --sky-top: #85abd2;
    --sky-deep: #2c3f55;
  }
  * { box-sizing: border-box; margin: 0; padding: 0; }
  html, body { width: 1200px; height: 915px; overflow: hidden; background: var(--backdrop); }
  body { position: relative; font-family: "Roboto", Arial, sans-serif; color: var(--ink); }

  .spread { position: absolute; width: 582px; height: 290px; background: var(--paper); overflow: hidden; }
  .col-left { left: 12px; } .col-right { left: 605px; }
  .row-1 { top: 12px; } .row-2 { top: 313px; } .row-3 { top: 614px; }

  .photo { position: absolute; width: 112px; height: 112px; }
  .body-copy { position: absolute; font-size: 9.4px; line-height: 1.2; }
  .body-copy p + ul, .body-copy p + ol { margin-top: 3px; }
  .scripture { list-style: disc; padding-left: 14px; font-style: italic; font-size: 7.8px; line-height: 1.15; color: var(--ink-soft); }
  .truths { padding-left: 16px; font-size: 7.8px; line-height: 1.1; }
  .page-no { position: absolute; top: 262px; font-size: 7.5px; font-style: italic; color: var(--ink-soft); }

  .cover-title { position: absolute; left: 452px; top: 106px; font-size: 20px; line-height: 1.15; color: #3a3a3a; }
  .cover-title strong { font-weight: 700; }

  .verse-panel { position: absolute; left: 291px; top: 0; width: 291px; height: 290px;
    background: linear-gradient(180deg, #4f6f8f 0%, var(--sky-top) 35%, #5d7a96 60%, var(--sky-deep) 100%); }
  .verse-panel .verse { position: absolute; left: 0; width: 100%; text-align: center; color: var(--paper);
    font-family: "Oswald", "Arial Narrow", sans-serif; font-style: italic; letter-spacing: -0.3px; }
  .verse-ref { position: absolute; left: 0; width: 100%; top: 254px; text-align: center; color: var(--paper); font-size: 8px; }
</style>
</head>
<body>

<!-- Cover -->
<section class="spread col-left row-1">
  <div class="photo" role="img" aria-label="Fresco of two outstretched hands reaching toward each other" style="left:158px;top:90px;width:253px;height:112px;background:linear-gradient(90deg,#a58a6a,#d8c7a8 45%,#c9a98a 70%,#8e3b40);"></div>
  <h1 class="cover-title"><strong>Lanterns</strong><br>Over<br><strong>Millbrook</strong></h1>
</section>

<!-- Pages 2–3 -->
<section class="spread col-right row-1">
  <div class="photo" role="img" aria-label="Colourful nebula in deep space" style="left:90px;top:90px;background:radial-gradient(circle at 55% 50%,#e9e2e6,#a07a8e 35%,#3f5a4c 70%,#1d2a2a);"></div>
  <div class="body-copy" style="left:376px;top:106px;width:150px;">
    <p><strong>God</strong> willingly created the universe, meaning he envisioned, designed, and made us.</p>
    <ul class="scripture"><li>“In the beginning God created the heavens and the earth.” (Genesis 1:1)”</li></ul>
  </div>
  <span class="page-no" style="left:29px;">2</span>
  <span class="page-no" style="left:552px;">3</span>
</section>

<!-- Pages 4–5 -->
<section class="spread col-left row-2">
  <div class="photo" role="img" aria-label="Open book with two pages curled into a heart shape" style="left:90px;top:30px;background:linear-gradient(180deg,#e6e2dc,#b9b3aa 55%,#3a3633);"></div>
  <div class="body-copy" style="left:30px;top:157px;width:240px;">
    <p>This reality establishes some foundational truths for all of us:</p>
    <ol class="truths">
      <li>God loves us - he didn’t have to create us; we are here because he couldn’t imagine life without us.</li>
      <li>God is the proper authority in our lives - if he designed and made us, he rightfully owns us.</li>
      <li>God knows the purpose of our lives - if he designed and made us, he knows why we are here.</li>
      <li>God’s truth is the truth we need - if he designed and made us, he knows what it takes for life to go well for us.</li>
    </ol>
  </div>
  <div class="body-copy" style="left:322px;top:45px;width:230px;">
    <p>But we, mankind, have all rejected God’s authority in our lives. And because he rightfully owns us, our rebellion against God is a grave injustice; an act of treason for which we deserve to be cut off from God forever.</p>
    <ul class="scripture"><li>“For the wages of sin is death…” (Romans 6:23)</li></ul>
  </div>
  <div class="photo" role="img" aria-label="Small wooden cross bound with string beside a folded cloth" style="left:381px;top:134px;background:linear-gradient(135deg,#8a7a6a,#b9a48c 50%,#6f5f52);"></div>
  <span class="page-no" style="left:30px;">4</span>
  <span class="page-no" style="left:552px;">5</span>
</section>

<!-- Pages 6–7 -->
<section class="spread col-right row-2">
  <div class="body-copy" style="left:35px;top:39px;width:228px;">
    <p>This alienation from God is evident in a myriad of ways including poverty, crime, conflict in our relationships, and our internal struggles. But worse, when we die, we must face the consequences for our rejection of God by spending eternity in hell - a lake of fire created by God as the place where our treason is brought to justice.</p>
  </div>
  <div class="photo" role="img" aria-label="Silhouetted person holding head in hands against a sunset" style="left:90px;top:139px;background:radial-gradient(circle at 60% 40%,#f2c276,#b46a2a 40%,#2a1a12 80%);"></div>
  <div class="photo" role="img" aria-label="Person with arms raised toward a golden sky" style="left:381px;top:34px;background:radial-gradient(circle at 50% 25%,#fff4c2,#e0c063 45%,#6b5a2a 90%);"></div>
  <div class="body-copy" style="left:322px;top:157px;width:225px;">
    <p>But God does not want you to pay for your own sins. God loves us so much he sent his only son to save us. Jesus Christ died on the cross to serve our sentence for our rebellion against God and rose again on the third day. Since Christ paid our full penalty, we can be completely forgiven and reconciled to God.</p>
    <ul class="scripture"><li>“For God so loved the world that he sent his one and only son that whosoever believes in him will not perish but have eternal life.” (John 3:16)</li></ul>
  </div>
  <span class="page-no" style="left:29px;">6</span>
  <span class="page-no" style="left:552px;">7</span>
</section>

<!-- Pages 8–9 -->
<section class="spread col-left row-3">
  <div class="photo" role="img" aria-label="Silhouette of a kneeling person praying in morning mist" style="left:90px;top:33px;background:linear-gradient(90deg,#f3ede4,#b8ab98 45%,#2e2a26);"></div>
  <div class="body-copy" style="left:30px;top:172px;width:252px;font-size:9.6px;">
    <p>Here is what you must do to be saved: First, ask Jesus Christ to save you (Since he is God, he can hear you): Acknowledge that God is the rightful authority of the universe and your life. Apologize to him for your rebellion against God.</p>
  </div>
  <div class="photo" role="img" aria-label="Woman with folded hands praying beside a brick wall" style="left:381px;top:33px;background:linear-gradient(90deg,#8a5a44,#c79a6e 45%,#5a3a2a);"></div>
  <div class="body-copy" style="left:322px;top:172px;width:240px;font-size:9.6px;">
    <p>Ask Jesus Christ to come into your life as your Lord and Savior. This decision will immediately trigger his miracle of salvation in you. God now lives in you!</p>
    <ul class="scripture"><li>“If you confess with your mouth that Jesus is Lord and believe in your heart that God raised him from the dead, you will be saved.” (Romans 10:9)</li></ul>
  </div>
  <span class="page-no" style="left:29px;">8</span>
  <span class="page-no" style="left:552px;">9</span>
</section>

<!-- Pages 10–11 -->
<section class="spread col-right row-3">
  <div class="body-copy" style="left:30px;top:102px;width:235px;font-size:9.6px;line-height:1.25;">
    <p>Next, God has given us the Bible and his church as the key tools for us to grow in our understanding of God and our personal relationship with him. So, it is essential you find a local church that believes the Bible is 100% true. Tell one of the pastors you are a brand new Christian and they will help you from there.</p>
  </div>
  <div class="verse-panel" role="img" aria-label="Layered blue mountain ridges under a misty sky">
    <p class="verse" style="top:89px;font-size:8px;">IF YOU CONFESS WITH YOUR MOUTH,</p>
    <p class="verse" style="top:109px;font-size:14px;">“JESUS IS LORD,”</p>
    <p class="verse" style="top:138px;font-size:8px;line-height:1.45;">AND BELIEVE IN YOUR HEART THAT GOD RAISED HIM<br>FROM THE DEAD,</p>
    <p class="verse" style="top:168px;font-size:13px;">YOU WILL BE SAVED.</p>
    <p class="verse-ref">ROMANS 10:9</p>
  </div>
  <span class="page-no" style="left:29px;">10</span>
</section>

</body>
</html>
```